Re-design and craft the perfect CV platform

We are building a CV-based platform designed to connect employees and employers, with a strong focus on individual users. As we're just starting out, we're looking to have our platform and logo redesigned to better reflect our vision
https://app.plovanstaffing.com/
Colors like in the logo attached
#87C032 #6A6E71 #618930 - also you can add more colors if you like.
https://app.plovanstaffing.com/dashboard - This page would be nice if you plan it, like personal Bio dashboard. Attached picture (Dashboard wanted) one idea from how we would like to be, but we are open for new professional ideas/solutions.
https://app.plovanstaffing.com/posts - On this page we want to be showed the jobs posted. Attached one picture about our idea (jobs page wanted)
https://app.plovanstaffing.com/profile - design something nice.
Only Photoshop, Illustrator or Framely
Other pictures from the app attached (as looking right now)

Target Market(s)

Job seekers, HR, Recruiters

Industry/Entity Type

HR Tech

Number of Pages Required

5+ page

Colors
00AB8E
00BBA5
67D7C9
C6EFE9
E9F9F6

```html
<!DOCTYPE html>
<html lang="en">
<head>
<meta charset="utf-8">
<title>Plovan – Dashboard</title>
<link href="https://fonts.googleapis.com/css2?family=Poppins:wght@400;500;600;700&display=swap" rel="stylesheet">
<style>
:root{
  --teal:#00ab8e;
  --teal-2:#00a693;
  --lime:#8dc63f;
  --green-ok:#6cc04a;
  --ink:#1d1d1d;
  --muted:#a6a6a6;
  --line:#e3e3e3;
  --page:#f2f5f4;
  --chip:#ececec;
  --bar:#f4f4f4;
  --select:#d9d9d9;
}
*{box-sizing:border-box;margin:0;padding:0}
html,body{width:675px;height:1200px;overflow:hidden;background:var(--page)}
body{font-family:'Poppins',sans-serif;color:var(--ink)}
.stage{width:1280px;height:2276px;transform:scale(.52734);transform-origin:0 0;position:relative;background:var(--page)}
.abs{position:absolute}
/* header */
.topbar{left:0;top:0;width:1280px;height:95px;background:#fff}
.brand{left:40px;top:26px;display:flex;align-items:center;gap:10px;font-size:34px;font-weight:600;color:var(--ink)}
.brand-dot{width:32px;height:32px;border-radius:50%;background:var(--teal)}
.nav{right:50px;top:35px;display:flex;align-items:center;gap:22px;font-size:14px}
.nav .active{color:var(--teal);font-weight:600}
.searchbar{left:0;top:96px;width:1280px;height:77px;background:var(--bar);border-top:2px solid #e6e6e6;border-bottom:2px solid #e6e6e6}
.find{left:59px;top:28px;font-size:17px}
.select{top:17px;width:250px;height:41px;background:var(--select);font-size:15px;padding:11px 18px;display:flex;justify-content:space-between;align-items:center}
.btn-search{left:1056px;top:17px;width:159px;height:41px;background:var(--teal);color:#fff;font-size:15px;display:flex;align-items:center;justify-content:center;gap:12px}
/* hero */
.hero{left:0;top:185px;width:1280px;height:226px;background:linear-gradient(90deg,var(--teal-2) 0%,#3fb874 45%,var(--lime) 100%);color:#fff}
.avatar{left:78px;top:34px;width:167px;height:167px;border-radius:50%;background:#fff}
.avatar-fill{left:34px;top:22px;width:100px;height:122px;border-radius:50px 50px 8px 8px;background:linear-gradient(180deg,#00a693,#0e9e88)}
.edit-badge{left:187px;top:162px;width:51px;height:51px;border-radius:50%;background:var(--teal);border:3px solid #fff;display:flex;align-items:center;justify-content:center}
.hero-name{left:268px;top:40px;font-size:26px;font-weight:700}
.hero-role{left:268px;top:73px;font-size:17px}
.hero-meta{left:268px;top:122px;font-size:17px;line-height:26px}
/* cards */
.card{left:40px;width:812px;background:#fff}
.card h2{font-size:18px;font-weight:500;display:flex;align-items:center;gap:9px;position:absolute;left:19px}
.card p,.card .txt{font-size:14px;line-height:21px}
.rule{left:19px;width:769px;height:1px;background:var(--line)}
.link{color:var(--teal);font-size:14px;font-weight:500}
.entry{font-size:13px;line-height:21px}
.entry b{font-weight:500}
.dim{color:var(--muted)}
.tag{display:inline-block;background:var(--teal);color:#fff;font-size:9px;padding:1px 10px;margin-left:10px;vertical-align:2px}
.chips{left:19px;top:108px;width:760px;display:flex;flex-wrap:wrap;gap:10px 10px}
.chip{background:var(--chip);border-radius:14px;height:28px;padding:0 10px 0 9px;font-size:14px;display:flex;align-items:center;gap:10px}
.chip i{width:16px;height:16px;border-radius:50%;background:#c9c9c9;color:#fff;font-style:normal;font-size:10px;display:flex;align-items:center;justify-content:center}
/* side */
.progress{left:878px;top:437px;width:362px;height:154px;background:var(--teal);color:#fff}
.side{left:878px;top:591px;width:362px;height:1320px;background:#fff}
.check-list{left:25px;top:20px;width:310px;font-size:14px}
.check-list li{list-style:none;display:flex;justify-content:space-between;align-items:center;height:31px}
.dot{width:22px;height:22px;border-radius:50%;background:#dcdcdc;display:flex;align-items:center;justify-content:center}
.dot.ok{background:var(--green-ok)}
.recent-head{left:25px;top:325px;width:312px;height:46px;background:#ececec;font-size:17px;font-weight:500;padding:11px 26px}
.post{left:13px;width:335px;border-left:2px solid var(--teal);padding-left:14px;font-size:13px;line-height:20px}
.post .t{color:var(--teal);font-weight:500}
.post .ago{position:absolute;right:2px;top:0;font-size:10px;color:var(--muted)}
.post b{font-weight:600}
.view-more{left:14px;top:1236px;width:333px;height:41px;background:var(--teal);color:#fff;font-size:15px;display:flex;align-items:center;justify-content:center;gap:10px}
.footer{left:0;top:2192px;width:1280px;height:84px;background:#fff;display:flex;justify-content:center;gap:14px;padding-top:24px;font-size:12px;color:#777}
</style>
</head>
<body>
<div class="stage">
  <header class="abs topbar">
    <div class="abs brand"><span class="brand-dot"></span>Plovan</div>
    <nav class="abs nav">
      <span class="active">Dashboard</span><span>My Job Application</span><span>Jobs</span><span>Profile</span><span>Help Center</span>
      <svg width="24" height="24" viewBox="0 0 24 24" fill="none" stroke="#00ab8e" stroke-width="1.8"><path d="M6 17V11a6 6 0 0 1 12 0v6l2 2H4z"/><path d="M10 21h4"/></svg>
      <svg width="24" height="22" viewBox="0 0 24 22" fill="none" stroke="#00ab8e" stroke-width="1.8"><rect x="2" y="4" width="20" height="16" rx="2"/><path d="M2 6l10 7 10-7"/></svg>
    </nav>
  </header>

  <section class="abs searchbar">
    <div class="abs find">Find a Job</div>
    <div class="abs select" style="left:180px">Any job functions <span>&#8964;</span></div>
    <div class="abs select" style="left:472px">Any Industries <span>&#8964;</span></div>
    <div class="abs select" style="left:764px">Any Experience level <span>&#8964;</span></div>
    <div class="abs btn-search">Search <span>&#x203A;</span></div>
  </section>

  <section class="abs hero">
    <div class="abs avatar"><div class="abs avatar-fill" role="img" aria-label="Profile photo placeholder"></div></div>
    <div class="abs edit-badge"><svg width="22" height="22" viewBox="0 0 24 24" fill="none" stroke="#fff" stroke-width="1.8"><rect x="3" y="4" width="16" height="16" rx="3"/><path d="M9 15l1-4 8-8 3 3-8 8z"/></svg></div>
    <div class="abs hero-name">Dorian Vale</div>
    <div class="abs hero-role">Expert Graphic UI/UX Designer</div>
    <div class="abs hero-meta">Experience: 5 years<br>Availability: Immediately<br>Location: New York</div>
  </section>

  <!-- Employment -->
  <section class="abs card" style="top:437px;height:169px">
    <h2 style="top:26px">Employment &amp; Availability</h2>
    <p class="abs" style="left:19px;top:60px;width:690px">Keeping this section up to date will help employers &amp; recruiters find you. They will know the field you are in, what your preferred industries are, and if you are actively looking.</p>
    <div class="abs rule" style="top:121px"></div>
    <div class="abs txt" style="left:19px;top:140px"><b style="font-weight:500">Status:</b> <span style="color:var(--teal)">Availability</span></div>
    <div class="abs link" style="right:55px;top:140px">Update Here</div>
  </section>

  <!-- About -->
  <section class="abs card" style="top:619px;height:226px">
    <h2 style="top:14px"><svg width="18" height="22" viewBox="0 0 18 22" fill="none" stroke="#1d1d1d" stroke-width="1.6"><circle cx="9" cy="6" r="5"/><path d="M1 21a8 8 0 0 1 16 0"/></svg>About Me</h2>
    <p class="abs" style="left:19px;top:48px;width:700px">Meet Dorian Vale, a versatile creative professional with a passion for transforming ideas into visually stunning and user-friendly digital experiences. With a background in graphic design and expertise in UI/UX (User Interface/User Experience) design, I bring a unique blend of</p>
    <div class="abs txt" style="left:19px;top:133px;font-weight:500">see more......</div>
    <div class="abs rule" style="top:178px"></div>
    <div class="abs link" style="right:55px;top:191px">Edit Here</div>
  </section>

  <!-- Work -->
  <section class="abs card" style="top:857px;height:445px">
    <h2 style="top:22px"><svg width="24" height="22" viewBox="0 0 24 22" fill="none" stroke="#1d1d1d" stroke-width="1.6"><rect x="1" y="5" width="22" height="16" rx="2"/><path d="M8 5V2h8v3M1 11h22"/></svg>Work Experience</h2>
    <p class="abs" style="left:19px;top:52px">Add your Work Experience. Such as an internship, part-time work or long term specialised experience.</p>
    <div class="abs rule" style="top:87px"></div>
    <div class="abs entry" style="left:19px;top:108px"><b>UI/UX Designer at Harwick Bank Plc</b><span class="tag">Most Recent</span><br>New York | July 2022 - Current <span class="dim">(2yrs 4months)</span><br>Mid level<br>Industry: Banking, Finance &amp; Insurance<br>Function: Creative &amp; Design</div>
    <div class="abs entry" style="left:391px;top:102px"><b>Graphic Designer at Brightline Business Consulting</b><br>New York | July 2022 - Current <span class="dim">(2yrs 4months)</span><br>Mid level<br>Industry: Banking, Finance &amp; Insurance<br>Function: Creative &amp; Design</div>
    <div class="abs rule" style="top:237px"></div>
    <div class="abs entry" style="left:19px;top:258px"><b>Graphic Designer at The Tamsin Group.</b><br>New York | July 2022 - Current <span class="dim">(2yrs 4months)</span><br>Mid level<br>Industry: Banking, Finance &amp; Insurance<br>Function: Creative &amp; Design</div>
    <div class="abs rule" style="top:379px"></div>
    <div class="abs link" style="left:19px;top:400px">Edit&nbsp; List</div>
    <div class="abs link" style="right:55px;top:400px">ADD MORE</div>
  </section>

  <!-- Education -->
  <section class="abs card" style="top:1315px;height:315px">
    <h2 style="top:24px"><svg width="28" height="30" viewBox="0 0 28 30" fill="none" stroke="#1d1d1d" stroke-width="1.6"><path d="M2 8l12-6 12 6-12 6z"/><path d="M6 10v6c4 3 12 3 16 0v-6"/><rect x="2" y="19" width="24" height="9" rx="1"/></svg>Education Background</h2>
    <p class="abs" style="left:19px;top:59px">List your qualifications here.</p>
    <div class="abs rule" style="top:89px"></div>
    <div class="abs entry" style="left:19px;top:102px"><b>Hollister University</b><br>BSc: Office Technology and Management<br>November 2013 - August 2015</div>
    <div class="abs entry" style="left:413px;top:102px"><b>Eastbrook University (EBU)</b><br>Masters: Office Technology and Management<br>November 2013 - August 2015</div>
    <div class="abs entry" style="left:19px;top:183px"><b>Hollister University</b><br>Phd: Office Technology and Management<br>November 2013 - August 2015</div>
    <div class="abs entry" style="left:413px;top:183px"><b>Hollister University</b><br>Diploma: Office Technology and Management<br>November 2013 - August 2015</div>
    <div class="abs rule" style="top:272px"></div>
    <div class="abs link" style="left:19px;top:279px">Edit&nbsp; List</div>
    <div class="abs link" style="right:55px;top:279px">ADD MORE</div>
  </section>

  <!-- Skills -->
  <section class="abs card" style="top:1643px;height:263px">
    <h2 style="top:24px"><svg width="26" height="26" viewBox="0 0 26 26" fill="none" stroke="#1d1d1d" stroke-width="1.6"><circle cx="9" cy="7" r="5"/><path d="M1 24a8 8 0 0 1 11-7"/><circle cx="19" cy="19" r="3"/><path d="M19 13v2M19 23v2M13 19h2M23 19h2"/></svg>Job Skills</h2>
    <p class="abs" style="left:19px;top:60px">What are your areas of expertise?</p>
    <div class="abs rule" style="top:89px"></div>
    <div class="abs chips">
      <span class="chip">Design Research <i>✕</i></span><span class="chip">Pixelry Studio <i>✕</i></span><span class="chip">Vectra Draw <i>✕</i></span><span class="chip">Framely <i>✕</i></span><span class="chip">UI/UX <i>✕</i></span>
      <span class="chip">Analytical thinking <i>✕</i></span><span class="chip">Decision-making <i>✕</i></span><span class="chip">Data analysis <i>✕</i></span><span class="chip">Strategic planning <i>✕</i></span>
      <span class="chip">Interpersonal skills <i>✕</i></span><span class="chip">Problem resolution <i>✕</i></span><span class="chip">Planning and executing <i>✕</i></span>
    </div>
    <div class="abs rule" style="top:227px"></div>
    <div class="abs link" style="right:55px;top:235px">ADD MORE</div>
  </section>

  <!-- Certificates -->
  <section class="abs card" style="top:1919px;height:226px">
    <h2 style="top:24px"><svg width="24" height="26" viewBox="0 0 24 26" fill="none" stroke="#1d1d1d" stroke-width="1.6"><rect x="3" y="2" width="18" height="22" rx="2"/><circle cx="9" cy="9" r="3"/><path d="M14 9h4M7 16h11M7 20h8"/></svg>Certificates &amp; Awards</h2>
    <p class="abs" style="left:19px;top:60px">Received any certificates or awards? Show them off to help enrich your career profile.</p>
    <div class="abs rule" style="top:89px"></div>
    <div class="abs entry" style="left:19px;top:101px"><b>Certified Project Lead (CPL)</b><br>Project Leadership Council (PLC)<br>November 2013 - August 2015</div>
    <div class="abs entry" style="left:356px;top:101px"><b>Certified Nursing Assistant (CNA)</b><br>Project Leadership Council (PLC)<br>November 2013 - August 2015</div>
    <div class="abs rule" style="top:181px"></div>
    <div class="abs link" style="right:55px;top:189px">ADD MORE</div>
  </section>

  <!-- Progress -->
  <aside class="abs progress">
    <svg class="abs" style="left:28px;top:10px" width="132" height="132" viewBox="0 0 132 132">
      <circle cx="66" cy="66" r="58" fill="none" stroke="#fff" stroke-width="4"/>
      <circle cx="66" cy="66" r="58" fill="none" stroke="#39d41a" stroke-width="8" stroke-dasharray="317 364" transform="rotate(-90 66 66)" stroke-linecap="round"/>
      <text x="66" y="80" text-anchor="middle" fill="#fff" font-family="Poppins,sans-serif" font-size="38" font-weight="600">87%</text>
    </svg>
    <div class="abs" style="left:178px;top:26px;font-size:18px;font-weight:600">Profile Progress</div>
    <div class="abs" style="left:178px;top:61px;font-size:14px;line-height:21px">Complete Your<br>Profile and Unlock<br>more job opportunities</div>
  </aside>
  <aside class="abs side">
    <ul class="abs check-list">
      <li>About me<span class="dot ok"><svg width="12" height="10" viewBox="0 0 12 10" fill="none" stroke="#fff" stroke-width="2"><path d="M1 5l3.5 3.5L11 1"/></svg></span></li>
      <li>Work Experience<span class="dot ok"><svg width="12" height="10" viewBox="0 0 12 10" fill="none" stroke="#fff" stroke-width="2"><path d="M1 5l3.5 3.5L11 1"/></svg></span></li>
      <li>Education<span class="dot ok"><svg width="12" height="10" viewBox="0 0 12 10" fill="none" stroke="#fff" stroke-width="2"><path d="M1 5l3.5 3.5L11 1"/></svg></span></li>
      <li>Job Skills<span class="dot ok"><svg width="12" height="10" viewBox="0 0 12 10" fill="none" stroke="#fff" stroke-width="2"><path d="M1 5l3.5 3.5L11 1"/></svg></span></li>
      <li>Profile Photo<span class="dot"></span></li>
      <li>Availability<span class="dot ok"><svg width="12" height="10" viewBox="0 0 12 10" fill="none" stroke="#fff" stroke-width="2"><path d="M1 5l3.5 3.5L11 1"/></svg></span></li>
      <li>Upload CV<span class="dot"></span></li>
      <li>Certificates &amp; Awards<span class="dot"></span></li>
      <li>Cover Letter<span class="dot"></span></li>
    </ul>
    <div class="abs recent-head">Recent Job Post</div>
    <div class="abs post" style="top:396px"><div class="t">Business Development Officer</div><span class="ago">2 days ago</span>Corrin And Associates<br><b>Job function:</b> Management &amp; Business Development</div>
    <div class="abs post" style="top:497px"><div class="t">Business Development Officer</div><span class="ago">2 days ago</span>Corrin And Associates<br><b>Job function:</b> Management &amp; Business Development</div>
    <div class="abs post" style="top:598px"><div class="t">Business Development Officer</div><span class="ago">2 days ago</span>Corrin And Associates<br><b>Job function:</b> Management &amp; Business Development</div>
    <div class="abs post" style="top:699px"><div class="t">Business Development Officer</div><span class="ago">2 days ago</span>Corrin And Associates<br><b>Job function:</b> Management &amp; Business Development</div>
    <div class="abs post" style="top:800px"><div class="t">Business Development Officer</div><span class="ago">2 days ago</span>Corrin And Associates<br><b>Job function:</b> Management &amp; Business Development</div>
    <div class="abs post" style="top:901px"><div class="t">Business Development Officer</div><span class="ago">2 days ago</span>Corrin And Associates<br><b>Job function:</b> Management &amp; Business Development</div>
    <div class="abs post" style="top:1002px"><div class="t">Business Development Officer</div><span class="ago">2 days ago</span>Corrin And Associates<br><b>Job function:</b> Management &amp; Business Development</div>
    <div class="abs post" style="top:1103px"><div class="t">Business Development Officer</div><span class="ago">2 days ago</span>Corrin And Associates<br><b>Job function:</b> Management &amp; Business Development</div>
    <div class="abs view-more">View More <span>&#x203A;</span></div>
  </aside>

  <footer class="abs footer">
    <span>About</span><span>|</span><span>Companies Hiring</span><span>|</span><span>Privacy Policy</span><span>|</span><span>Terms</span><span>|</span><span>CV Review</span><span>|</span><span>Skill Assessments</span>
  </footer>
</div>
</body>
</html>
```